TAILWIND FIELDS Pet Resorts Outdoor Signage

4 x 8 outdoor signage design for our two locations

Target Market(s)

Existing and New Customers

Industry/Entity Type

Pet Care

Font styles to use
Sans Serif

Colors

Designer to choose colors to be used in the design.

```html
<!DOCTYPE html>
<html lang="en">
<head>
<meta charset="utf-8">
<title>TAILWIND FIELDS Pet Resorts – Outdoor Sign</title>
<link rel="stylesheet" href="https://fonts.googleapis.com/css2?family=Montserrat:wght@400;500;600;700&display=swap">
<style>
  :root {
    --teal: #4b8fa1;
    --teal-dark: #2f6b7a;
    --ink: #3b3b3d;
    --white: #ffffff;
    --page: #efefef;
    --photo-light: #f4f3f0;
    --photo-mid: #c9b79c;
    --photo-dark: #6e5b45;
  }
  * { margin: 0; padding: 0; box-sizing: border-box; }
  html, body { width: 1200px; height: 800px; overflow: hidden; }
  body {
    background: var(--page);
    font-family: "Montserrat", Arial, sans-serif;
    position: relative;
  }
  .sign {
    position: absolute;
    left: 420px;
    top: 40px;
    width: 360px;
    height: 720px;
    background: var(--white);
    box-shadow: 0 10px 24px rgba(0,0,0,0.22);
    overflow: hidden;
  }
  .sign-shapes { position: absolute; inset: 0; }
  .brand-name {
    position: absolute;
    left: 0;
    width: 290px;
    top: 48px;
    text-align: center;
    font-weight: 700;
    font-size: 27px;
    letter-spacing: 0.5px;
    line-height: 1.15;
    color: var(--ink);
  }
  .ribbon-text {
    position: absolute;
    left: 298px;
    width: 62px;
    top: 126px;
    text-align: center;
    color: var(--teal);
    font-weight: 600;
    font-size: 24px;
    line-height: 29px;
  }
  .ribbon-text span { display: block; }
  .ribbon-text .gap { height: 14px; }
  .services { position: absolute; left: 12px; top: 180px; list-style: none; }
  .services li {
    display: flex;
    align-items: center;
    height: 28px;
    margin-bottom: 29.5px;
    color: var(--white);
    font-weight: 700;
    font-size: 19px;
    letter-spacing: 0.3px;
  }
  .services svg { width: 16px; height: 16px; margin-right: 12px; flex: none; }
  .photo-dog {
    position: absolute;
    left: 205px;
    top: 478px;
    width: 155px;
    height: 147px;
    background: radial-gradient(ellipse at 60% 55%, var(--photo-dark) 0%, var(--photo-mid) 45%, var(--photo-light) 80%);
  }
  .tagline { position: absolute; left: 33px; top: 510px; color: var(--ink); }
  .tagline span { display: block; }
  .tagline .t1 { font-weight: 500; font-size: 23px; letter-spacing: 4px; line-height: 30px; }
  .tagline .t2 { font-weight: 500; font-size: 20px; letter-spacing: 3.5px; line-height: 30px; }
  .tagline .t3 { font-weight: 700; font-size: 28px; letter-spacing: 1px; line-height: 34px; }
  .contact {
    position: absolute;
    left: 0; right: 0;
    top: 640px;
    text-align: center;
    color: var(--white);
  }
  .phone { font-weight: 600; font-size: 33px; letter-spacing: 0.5px; line-height: 40px; }
  .web { font-weight: 600; font-size: 13px; letter-spacing: 2.5px; margin-top: 6px; }
</style>
</head>
<body>
  <div class="sign">
    <svg class="sign-shapes" viewBox="0 0 360 720" width="360" height="720" aria-hidden="true">
      <path d="M0 138 Q 120 120 235 124 Q 270 126 298 132 L360 130 L360 472 Q 250 478 160 482 Q 70 486 0 494 Z" fill="var(--teal)"/>
      <rect x="0" y="625" width="360" height="95" fill="var(--teal)"/>
      <polygon points="288,122 298,108 298,122" fill="var(--teal-dark)"/>
      <polygon points="298,108 360,108 360,437 329,412 298,437" fill="var(--white)"/>
    </svg>

    <div class="brand-name">TAILWIND<br>FIELDS</div>

    <div class="ribbon-text">
      <span>P</span><span>E</span><span>T</span>
      <span class="gap"></span>
      <span>R</span><span>E</span><span>S</span><span>O</span><span>R</span><span>T</span>
    </div>

    <ul class="services">
      <li><svg viewBox="0 0 16 16" aria-hidden="true"><g fill="var(--white)"><ellipse cx="8" cy="11" rx="4" ry="3.4"/><circle cx="3" cy="6.5" r="1.7"/><circle cx="6" cy="3.5" r="1.7"/><circle cx="10" cy="3.5" r="1.7"/><circle cx="13" cy="6.5" r="1.7"/></g></svg>BOARDING</li>
      <li><svg viewBox="0 0 16 16" aria-hidden="true"><g fill="var(--white)"><ellipse cx="8" cy="11" rx="4" ry="3.4"/><circle cx="3" cy="6.5" r="1.7"/><circle cx="6" cy="3.5" r="1.7"/><circle cx="10" cy="3.5" r="1.7"/><circle cx="13" cy="6.5" r="1.7"/></g></svg>DAYCARE</li>
      <li><svg viewBox="0 0 16 16" aria-hidden="true"><g fill="var(--white)"><ellipse cx="8" cy="11" rx="4" ry="3.4"/><circle cx="3" cy="6.5" r="1.7"/><circle cx="6" cy="3.5" r="1.7"/><circle cx="10" cy="3.5" r="1.7"/><circle cx="13" cy="6.5" r="1.7"/></g></svg>TRAINING</li>
      <li><svg viewBox="0 0 16 16" aria-hidden="true"><g fill="var(--white)"><ellipse cx="8" cy="11" rx="4" ry="3.4"/><circle cx="3" cy="6.5" r="1.7"/><circle cx="6" cy="3.5" r="1.7"/><circle cx="10" cy="3.5" r="1.7"/><circle cx="13" cy="6.5" r="1.7"/></g></svg>FULL-SERVICE SALON</li>
      <li><svg viewBox="0 0 16 16" aria-hidden="true"><g fill="var(--white)"><ellipse cx="8" cy="11" rx="4" ry="3.4"/><circle cx="3" cy="6.5" r="1.7"/><circle cx="6" cy="3.5" r="1.7"/><circle cx="10" cy="3.5" r="1.7"/><circle cx="13" cy="6.5" r="1.7"/></g></svg>PET TAXI &amp; MORE</li>
    </ul>

    <div class="photo-dog" role="img" aria-label="Photo of a shepherd dog in profile, facing left with mouth open"></div>

    <div class="tagline">
      <span class="t1">ALL</span>
      <span class="t2">BREED</span>
      <span class="t3">FRIENDLY</span>
    </div>

    <div class="contact">
      <div class="phone">905-555-0147</div>
      <div class="web">WWW.TAILWINDFIELDS.CA</div>
    </div>
  </div>
</body>
</html>
```